I need a audit of my current site.. with suggestions and actions

My current site, www.brickwisely does not support the high tech industry we are in. I am seeking knowledge, direction and action, I will pay hourly or by job. I also need SEO help, driven with impact trusted deliverable, our clients have to trust us to do our job. We are like Vorlin to the construction industry, gathering their data for the lifecycle. Eliminating litigation, un wanted change orders and providing audit ready projects. Eveyone wins

Target Market(s)

Construction industry, Federal and Private

Industry/Entity Type

Construction industry, globally

Coding

Coded - Design and coding required

Number of Pages Required

5+ page

Font styles to use
Sans Serif

Colors
EE7325
F08F49
F5BC92
FAE3D3
FDF4ED

Requirements
Must have
• High tech look
Should not have
• Misspelled words

```html
<!DOCTYPE html>
<html lang="en">
<head>
<meta charset="utf-8">
<title>BrickWisely — The Ultimate Construction Technology</title>
<link rel="stylesheet" href="https://fonts.googleapis.com/css2?family=Montserrat:wght@500;600;700;800;900&family=Work+Sans:wght@400;500;600&display=swap">
<style>
:root{
  --orange:#f29a1f;
  --orange-deep:#ee5a24;
  --brand:#ee7325;
  --blue:#1299d6;
  --blue-light:#55b6e4;
  --blue-mid:#1583bb;
  --blue-dark:#1f5f95;
  --navy:#0b1532;
  --navy-2:#0f2c5a;
  --ink:#111111;
  --text:#3b3b3b;
  --grey:#f1f1f1;
  --line:#d9d9d9;
  --white:#ffffff;
}
*{box-sizing:border-box;margin:0;padding:0}
html,body{width:1200px;height:4717px;overflow:hidden;background:var(--white)}
body{font-family:"Work Sans",Arial,sans-serif;color:var(--text)}
.page{position:relative;width:1200px;height:4717px;overflow:hidden}
.abs{position:absolute}
.h{font-family:"Montserrat",Arial,sans-serif;font-weight:800;color:var(--ink);text-transform:uppercase}

/* top bar */
.topbar{position:absolute;left:0;top:0;width:1200px;height:28px;background:#2b2b2b;color:#fff;font-size:13px}
.topbar .item{position:absolute;top:6px;display:flex;align-items:center;gap:8px}
.dot-ico{width:16px;height:16px;border-radius:50%;background:var(--orange);display:inline-block}
.login{position:absolute;left:1048px;top:4px;width:59px;height:21px;background:var(--orange);color:#fff;font-weight:600;font-size:12px;text-align:center;line-height:21px;border-radius:2px}

/* nav */
.nav{position:absolute;left:0;top:28px;width:1200px;height:76px;background:#fff}
.nav .shade{position:absolute;left:420px;top:0;width:780px;height:76px;background:#ececec;clip-path:polygon(40px 0,100% 0,100% 100%,0 100%)}
.logo{position:absolute;display:flex;align-items:center;gap:8px;font-family:"Work Sans",sans-serif;font-weight:400;color:var(--brand)}
.logo .sq{width:14px;height:14px;background:var(--brand)}
.nav .menu{position:absolute;left:465px;top:31px;display:flex;gap:0;font-size:15px;color:#333}
.nav .menu span{margin-right:24px}
.nav .phone{position:absolute;left:950px;top:26px;display:flex;align-items:center;gap:10px;font-size:15px;color:#333}
.phone-ico{width:30px;height:30px;border-radius:50%;background:var(--orange);display:flex;align-items:center;justify-content:center}

/* hero */
.hero{position:absolute;left:0;top:104px;width:1200px;height:600px}
.hero .photo{position:absolute;inset:0;background:
  radial-gradient(ellipse 60% 45% at 62% 80%, #e08a2a 0%, #a4571d 35%, rgba(40,30,25,0) 75%),
  linear-gradient(180deg,#2c2a2b 0%,#3a302a 45%,#5a3a20 75%,#1f1a18 100%)}
.hero .kicker{position:absolute;left:88px;top:96px;color:#fff;font-family:"Montserrat",sans-serif;font-weight:800;font-size:22px;letter-spacing:.5px}
.hero h1{position:absolute;left:88px;top:122px;color:#fff;font-family:"Montserrat",sans-serif;font-weight:900;font-size:64px;line-height:68px}
.hero ul{position:absolute;left:92px;top:277px;list-style:none;color:#fff;font-size:15px;line-height:25.6px}
.hero li{display:flex;align-items:center;gap:12px}
.btn{display:inline-block;font-family:"Montserrat",sans-serif;font-weight:700;text-transform:uppercase;text-align:center}
.hero .cta{position:absolute;left:92px;top:424px;width:181px;height:55px;line-height:55px;background:var(--orange);color:#fff;font-size:14px}
.hero .pager{position:absolute;left:1096px;top:298px;display:flex;flex-direction:column;gap:14px}
.hero .pager i{width:10px;height:10px;border-radius:50%;border:1.5px solid #ddd;display:block}
.hero .pager i.on{background:var(--orange);border-color:var(--orange)}

/* about */
.about-name{position:absolute;font-family:"Montserrat",sans-serif;font-size:13px;color:#222;line-height:18px}
.about-name b{font-weight:800}
.about-name span{font-weight:600;color:#555}
.about-title{position:absolute;left:599px;top:852px;font-size:33px}
.about-copy{position:absolute;left:599px;top:900px;width:505px;font-size:14.5px;line-height:25.6px;color:#3a3a3a}
.about-copy p{margin-bottom:12px}
.btn-dark{position:absolute;background:#111;color:#fff;font-size:14px}

/* why */
.why{position:absolute;left:0;top:1343px;width:1200px;height:410px}
.why .photo{position:absolute;inset:0;background:linear-gradient(120deg,#2d3338 0%,#4c5459 45%,#3b4247 100%)}
.why .panel{position:absolute;inset:0;background:var(--blue);clip-path:polygon(531px 379px,751px 77px,1200px 77px,1200px 379px)}
.why h2{position:absolute;right:81px;top:176px;text-align:right;color:#fff;font-family:"Montserrat",sans-serif;font-weight:800;font-size:32px;line-height:47px}

/* features */
.features{position:absolute;left:0;top:1753px;width:1200px;height:570px;background:linear-gradient(180deg,#ffffff 0%,#ececec 100%)}
.features svg text{font-family:"Montserrat",sans-serif;font-weight:700;fill:#fff;font-size:8px}

/* milestones */
.milestones{position:absolute;left:0;top:2323px;width:1200px;height:372px;background:var(--navy)}
.milestones h2{position:absolute;left:0;width:1200px;top:75px;text-align:center;color:#fff;font-size:31px}
.stat{position:absolute;top:145px;width:325px;height:152px;background:linear-gradient(180deg,#d6d6d6,#b9b9b9);text-align:center}
.stat .tab{position:absolute;left:130px;top:0;width:66px;height:44px;background:var(--blue);clip-path:polygon(0 0,100% 0,100% 72%,50% 100%,0 72%)}
.stat .num{position:absolute;left:0;width:100%;top:52px;font-family:"Montserrat",sans-serif;font-weight:800;font-size:44px;color:var(--ink)}
.stat .lbl{position:absolute;left:0;width:100%;top:112px;font-family:"Montserrat",sans-serif;font-weight:800;font-size:19px;color:var(--ink)}

/* platforms */
.plat-kicker{position:absolute;left:90px;top:2843px;font-size:22px}
.plat-title{position:absolute;left:90px;top:2876px;font-size:33px;line-height:47px}
.crane{position:absolute;left:690px;top:2790px;width:420px;height:230px;background:linear-gradient(90deg,rgba(200,200,200,.25),rgba(200,200,200,.45))}
.tile{position:absolute;width:240px;height:98px;background:#fff;border:1px solid #e3e3e3;box-shadow:0 2px 6px rgba(0,0,0,.12);display:flex;align-items:center;justify-content:center;font-family:"Montserrat",sans-serif;font-weight:700;font-size:25px;color:#222}
.dots{position:absolute;left:576px;top:3313px;display:flex;gap:9px}
.dots i{width:10px;height:10px;border-radius:50%;border:1.5px solid #999;display:block}
.dots i.on{background:var(--orange);border-color:var(--orange)}

/* bridge */
.bridge{position:absolute;left:0;top:3386px;width:1200px;height:425px;background:linear-gradient(90deg,#f6a21f 0%,#f28a22 50%,#ee5a24 100%)}
.bridge .cut{position:absolute;inset:0;background:#fff;clip-path:polygon(0 0,1200px 0,1200px 98px,600px 98px,575px 0,0 0,0 0)}
.bridge .cut2{position:absolute;inset:0;background:#fff;clip-path:polygon(0 425px,0 340px,90px 340px,170px 425px)}
.bridge .video{position:absolute;left:92px;top:50px;width:489px;height:300px;background:#f4f4f4;border:2px solid #333;box-shadow:0 6px 14px rgba(0,0,0,.3)}
.bridge .video .shot{position:absolute;left:8px;top:18px;right:18px;bottom:10px;background:linear-gradient(160deg,#a9c3d8 0%,#6d7f8e 55%,#3b4550 100%)}
.play{position:absolute;left:200px;top:104px;width:66px;height:66px;border-radius:50%;background:#e11b1b;display:flex;align-items:center;justify-content:center}
.bridge h2{position:absolute;right:92px;top:168px;text-align:right;color:#fff;font-size:32px;line-height:43px}
.bridge .gov{position:absolute;left:846px;top:309px;width:261px;height:55px;line-height:55px;background:#111;color:#fff;font-size:14px}

/* contact */
.contact-title{position:absolute;left:92px;top:3848px;font-size:31px}
.contact-copy{position:absolute;left:92px;top:3904px;width:420px;font-size:14.5px;line-height:25.6px;color:#3a3a3a}
.contact-copy p{margin-bottom:16px}
.seal{position:absolute;left:92px;top:4056px;width:160px;height:138px;border-radius:50%;background:radial-gradient(circle,#f0c22b 0%,#c9961a 70%,#8a6410 100%)}
.field{position:absolute;background:#fff;border:1px solid #cfcfcf;box-shadow:0 1px 4px rgba(0,0,0,.08);font-size:14px;color:#444;padding:18px 16px}
.btn-submit{position:absolute;left:597px;top:4091px;width:180px;height:53px;line-height:53px;background:#111;color:#fff;font-size:14px}

/* footer */
.footer{position:absolute;left:0;top:4232px;width:1200px;height:427px}
.footer .col{position:absolute;color:#fff;font-size:14.5px;line-height:26px}
.footer .lbl{display:flex;align-items:center;gap:8px}
.footer .rule{position:absolute;top:119px;width:1px;height:247px;background:#3b4563}
.legal{position:absolute;left:0;top:4659px;width:1200px;height:58px;background:#ececec}
.legal .copy{position:absolute;left:92px;top:20px;font-size:13px;color:#333}
.social{position:absolute;left:524px;top:12px;display:flex;gap:8px}
.social i{width:32px;height:32px;border-radius:50%;background:#444;display:block}
.certs{position:absolute;left:800px;top:8px;display:flex;gap:12px;align-items:center}
</style>
</head>
<body>
<div class="page">

  <!-- top bar -->
  <div class="topbar">
    <div class="item" style="left:92px"><span class="dot-ico"></span>marla@brickwisely.com &nbsp;/ support@brickwisely.com</div>
    <div class="item" style="left:640px">
      <svg width="16" height="18" viewBox="0 0 16 18"><path d="M8 1a6 6 0 0 0-6 6c0 4.5 6 10 6 10s6-5.5 6-10a6 6 0 0 0-6-6z" fill="#f29a1f"/><circle cx="8" cy="7" r="2.2" fill="#2b2b2b"/></svg>
      412 Halden Street Riverton, KS 66210</div>
    <div class="login">Log In</div>
  </div>

  <!-- navigation -->
  <div class="nav">
    <div class="shade"></div>
    <div class="logo" style="left:88px;top:20px;font-size:30px"><span class="sq"></span>BrickWisely</div>
    <div class="menu"><span>What We Offer</span><span>Portfolio</span><span>About</span><span>Podcast</span><span>Blogs</span></div>
    <div class="phone"><span class="phone-ico"><svg width="16" height="16" viewBox="0 0 24 24"><path d="M6.6 10.8a15 15 0 0 0 6.6 6.6l2.2-2.2a1 1 0 0 1 1-.25 11 11 0 0 0 3.6.6 1 1 0 0 1 1 1V20a1 1 0 0 1-1 1A17 17 0 0 1 3 4a1 1 0 0 1 1-1h3.5a1 1 0 0 1 1 1 11 11 0 0 0 .6 3.6 1 1 0 0 1-.25 1z" fill="#fff"/></svg></span>(816) 555-0148</div>
  </div>

  <!-- hero -->
  <section class="hero">
    <div class="photo" role="img" aria-label="Construction site with cranes and workers silhouetted against a sunset sky"></div>
    <div class="kicker">BUILD WITH THE ULTIMATE IN</div>
    <h1>Construction<br>Technology</h1>
    <ul>
      <li><svg width="14" height="12" viewBox="0 0 14 12"><path d="M1 6l4 4 8-9" stroke="#fff" stroke-width="2.2" fill="none"/></svg>Must solve problems not create them!</li>
      <li><svg width="14" height="12" viewBox="0 0 14 12"><path d="M1 6l4 4 8-9" stroke="#fff" stroke-width="2.2" fill="none"/></svg>Build 10xs faster</li>
      <li><svg width="14" height="12" viewBox="0 0 14 12"><path d="M1 6l4 4 8-9" stroke="#fff" stroke-width="2.2" fill="none"/></svg>Build with actionable data</li>
      <li><svg width="14" height="12" viewBox="0 0 14 12"><path d="M1 6l4 4 8-9" stroke="#fff" stroke-width="2.2" fill="none"/></svg>Prepared for discovery in litigation</li>
      <li><svg width="14" height="12" viewBox="0 0 14 12"><path d="M1 6l4 4 8-9" stroke="#fff" stroke-width="2.2" fill="none"/></svg>Lower bond rate</li>
    </ul>
    <div class="btn cta">Contact Us</div>
    <div class="pager"><i class="on"></i><i></i><i></i></div>
    <svg class="abs" style="left:0;top:530px" width="1200" height="70" viewBox="0 0 1200 70">
      <polygon points="0,20 560,56 1200,0 1200,14 560,70 0,36" fill="#f29a1f"/>
      <polygon points="0,36 560,70 1200,14 1200,70 0,70" fill="#fff"/>
    </svg>
  </section>

  <!-- about -->
  <svg class="abs" style="left:70px;top:840px" width="500" height="460" viewBox="70 840 500 460">
    <polygon points="235,858 361,931 361,1077 235,1150 109,1077 109,931" fill="#fff" stroke="#e6e6e6" stroke-width="3"/>
    <polygon points="235,870 351,937 351,1071 235,1138 119,1071 119,937" fill="#9c8f86" role="img" aria-label="Portrait photo of Marla J. Keswick, CEO and Founder"/>
    <polygon points="421,995 535,1061 535,1193 421,1259 307,1193 307,1061" fill="#fff" stroke="#e6e6e6" stroke-width="3"/>
    <polygon points="421,1007 525,1067 525,1187 421,1247 317,1187 317,1067" fill="#7d8a8f" role="img" aria-label="Portrait photo of Victor Keswick, President and Founder"/>
    <path d="M270 898 C310 870 340 875 380 885" stroke="#222" stroke-width="2.5" fill="none"/>
    <path d="M370 876 L382 886 L368 893" stroke="#222" stroke-width="2.5" fill="none"/>
    <path d="M450 1220 C430 1265 390 1270 322 1265" stroke="#222" stroke-width="2.5" fill="none"/>
    <path d="M334 1256 L320 1265 L333 1274" stroke="#222" stroke-width="2.5" fill="none"/>
  </svg>
  <div class="about-name" style="left:394px;top:864px"><b>MARLA J. KESWICK,</b><br><span>CEO &amp; FOUNDER</span></div>
  <div class="about-name" style="left:110px;top:1239px;text-align:right;width:192px"><b>VICTOR KESWICK</b><br><span>PRESIDENT &amp; FOUNDER</span></div>
  <h2 class="h about-title">About Us</h2>
  <div class="about-copy">
    <p>Victor and Marla Keswick knew that there had to be a better way to do construction. The management of documents is daunting yet mandatory. The more technology that was brought to the project, the bigger the challenge becomes. Accurate information is the real key.</p>
    <p>Today’s construction projects are too complex for traditional management techniques. Chaos cuts into bottom lines and into your sanity. The most successful construction management companies rely on software that can provide clear value by improving efficiency and ease of use.</p>
  </div>
  <div class="btn btn-dark" style="left:599px;top:1193px;width:181px;height:55px;line-height:55px">Read More</div>

  <!-- why -->
  <section class="why">
    <div class="photo" role="img" aria-label="Construction engineers in hard hats reviewing plans"></div>
    <div class="panel"></div>
    <h2>WHY WE ARE THE<br>BEST CONSTRUCTION<br>MANAGEMENT SOFTWARE</h2>
  </section>

  <!-- features diagram -->
  <section class="features">
    <svg width="1200" height="570" viewBox="0 957 655 311">
      <defs>
        <linearGradient id="dia" x1="0" y1="0" x2="1" y2="1"><stop offset="0" stop-color="#3bb0e6"/><stop offset="1" stop-color="#0d5f9c"/></linearGradient>
        <linearGradient id="diaDark" x1="0" y1="0" x2="1" y2="1"><stop offset="0" stop-color="#1d4f8a"/><stop offset="1" stop-color="#0b1f45"/></linearGradient>
      </defs>
      <!-- banners -->
      <polygon points="143,983 275,983 250,1019 143,1019" fill="#5db9e6"/>
      <polygon points="380,983 510,983 510,1019 405,1019" fill="#5db9e6"/>
      <polygon points="95,1036 230,1036 205,1071 95,1071" fill="#1aa0d8"/>
      <polygon points="425,1036 560,1036 560,1071 450,1071" fill="#1aa0d8"/>
      <polygon points="50,1095 185,1095 160,1133 50,1133" fill="#1383b8"/>
      <polygon points="470,1095 604,1095 604,1133 495,1133" fill="#1383b8"/>
      <polygon points="60,1158 215,1158 240,1195 60,1195" fill="#2a6aa1"/>
      <polygon points="432,1158 595,1158 595,1195 410,1195" fill="#2a6aa1"/>
      <polygon points="117,1212 278,1212 303,1248 117,1248" fill="#0f2c5a"/>
      <polygon points="375,1212 538,1212 538,1248 350,1248" fill="#0f2c5a"/>
      <text x="204" y="1004" text-anchor="middle">FINISH ON TIME</text>
      <text x="453" y="1004" text-anchor="middle">BIDDING PROCESS</text>
      <text x="148" y="1057" text-anchor="middle">STAY ON BUDGET</text>
      <text x="508" y="1051" text-anchor="middle">HOLD EVERYONE</text>
      <text x="512" y="1062" text-anchor="middle">ACCOUNTABLE</text>
      <text x="117" y="1113" text-anchor="middle">PROJECT</text>
      <text x="108" y="1125" text-anchor="middle">INFORMATION</text>
      <text x="565" y="1112" text-anchor="middle">CLOSEOUT</text>
      <text x="570" y="1124" text-anchor="middle">MODULE</text>
      <text x="145" y="1176" text-anchor="middle">TRACK (&amp; SEARCH)</text>
      <text x="155" y="1188" text-anchor="middle">DOCUMENTS</text>
      <text x="550" y="1179" text-anchor="middle">EASE OF USE</text>
      <text x="213" y="1233" text-anchor="middle">SECURITY</text>
      <text x="489" y="1233" text-anchor="middle">CUSTOMIZATION</text>
      <!-- centre diamond -->
      <polygon points="327,1030 411,1114 327,1198 243,1114" fill="#fff" stroke="#0f2c5a" stroke-width="2"/>
      <rect x="282" y="1109" width="6" height="6" fill="#ee7325"/>
      <text x="292" y="1117" style="font-family:'Work Sans',sans-serif;font-weight:400;fill:#ee7325;font-size:10px">BrickWisely</text>
      <!-- small diamonds -->
      <g stroke="#fff" stroke-width="2.5">
        <polygon points="284,987 317,1020 284,1053 251,1020" fill="url(#dia)"/>
        <polygon points="370,987 403,1020 370,1053 337,1020" fill="url(#dia)"/>
        <polygon points="235,1039 268,1072 235,1105 202,1072" fill="url(#dia)"/>
        <polygon points="418,1039 451,1072 418,1105 385,1072" fill="url(#dia)"/>
        <polygon points="188,1082 221,1115 188,1148 155,1115" fill="url(#dia)"/>
        <polygon points="465,1082 498,1115 465,1148 432,1115" fill="url(#dia)"/>
        <polygon points="236,1127 269,1160 236,1193 203,1160" fill="url(#diaDark)"/>
        <polygon points="418,1127 451,1160 418,1193 385,1160" fill="url(#diaDark)"/>
        <polygon points="284,1179 317,1212 284,1245 251,1212" fill="url(#diaDark)"/>
        <polygon points="370,1179 403,1212 370,1245 337,1212" fill="url(#diaDark)"/>
      </g>
      <!-- icons -->
      <g stroke="#fff" stroke-width="1.3" fill="none">
        <circle cx="284" cy="1021" r="8"/><path d="M284 1016v5l3 2"/>
        <rect x="362" y="1013" width="7" height="6"/><rect x="372" y="1021" width="7" height="6"/><path d="M369 1016h5v5"/>
        <rect x="229" y="1067" width="12" height="10"/><path d="M235 1069v6M233 1070h4"/>
        <rect x="412" y="1064" width="12" height="15"/><path d="M415 1068h6M415 1072h6M415 1076h6"/>
        <circle cx="188" cy="1115" r="6"/><circle cx="188" cy="1115" r="2"/>
        <rect x="457" y="1108" width="16" height="11"/><path d="M462 1123h6"/>
        <path d="M236 1152a5 5 0 0 1 5 5c0 4-5 9-5 9s-5-5-5-9a5 5 0 0 1 5-5z"/>
        <path d="M412 1164l6-8 6 8M418 1156v10"/>
        <path d="M284 1203l8 3v5c0 5-4 8-8 10-4-2-8-5-8-10v-5z"/><path d="M280 1212l3 3 5-5"/>
        <rect x="363" y="1205" width="14" height="14"/><circle cx="370" cy="1212" r="3"/>
      </g>
    </svg>
  </section>

  <!-- milestones -->
  <section class="milestones">
    <h2 class="h">Milestones</h2>
    <div class="stat" style="left:92px"><div class="tab"></div><div class="num">16</div><div class="lbl">YEARS IN BUSINESS</div></div>
    <div class="stat" style="left:438px"><div class="tab"></div><div class="num">+ 2K</div><div class="lbl">PROJECTS COMPLETED</div></div>
    <div class="stat" style="left:782px"><div class="tab"></div><div class="num">$ 23B</div><div class="lbl">CONSTRUCTION VALUE</div></div>
  </section>

  <!-- platforms -->
  <div class="crane" role="img" aria-label="Faint line drawing of a tower crane"></div>
  <div class="h plat-kicker">We Improve All</div>
  <h2 class="h plat-title">Construction Management<br>Software Platforms</h2>
  <div class="tile" style="left:92px;top:3041px">Stackline</div>
  <div class="tile" style="left:350px;top:3041px">Dovetra</div>
  <div class="tile" style="left:606px;top:3041px">Planwright 360</div>
  <div class="tile" style="left:863px;top:3041px">Tarola</div>
  <div class="tile" style="left:92px;top:3158px">Crewdeck</div>
  <div class="tile" style="left:350px;top:3158px">Oakridge</div>
  <div class="tile" style="left:606px;top:3158px">Corvex</div>
  <div class="tile" style="left:863px;top:3158px">Framewise</div>
  <div class="dots"><i class="on"></i><i></i><i></i></div>

  <!-- bridge -->
  <section class="bridge">
    <div class="cut"></div>
    <div class="cut2"></div>
    <div class="video">
      <div class="shot" role="img" aria-label="Business team standing in front of a glass office building"></div>
      <div class="play"><svg width="20" height="22" viewBox="0 0 20 22"><polygon points="3,2 18,11 3,20" fill="#fff"/></svg></div>
    </div>
    <h2 class="h">Bridge the gap in<br>project management<br>software</h2>
    <div class="btn gov">Government Projects</div>
  </section>

  <!-- contact -->
  <h2 class="h contact-title">Contact Us</h2>
  <div class="contact-copy">
    <p>Using our array of services, you can finally alleviate the stress of managing large construction projects. Find out how BrickWisely solves</p>
    <p>the largest problems in project management and how you can benefit.</p>
  </div>
  <div class="seal" role="img" aria-label="Guarantee seal for protection from costly construction litigation"></div>
  <div class="field" style="left:595px;top:3856px;width:251px;height:55px">Name</div>
  <div class="field" style="left:857px;top:3856px;width:250px;height:55px">Email</div>
  <div class="field" style="left:595px;top:3930px;width:512px;height:146px">Message</div>
  <div class="btn btn-submit">Submit Now</div>

  <!-- footer -->
  <footer class="footer">
    <svg class="abs" style="left:0;top:0" width="1200" height="427" viewBox="0 0 1200 427">
      <polygon points="0,55 600,0 1200,55 1200,427 0,427" fill="#0b1532"/>
      <polygon points="0,48 600,-6 1200,48 1200,62 600,8 0,62" fill="#f29a1f"/>
    </svg>
    <div class="logo" style="left:92px;top:146px;font-size:28px;color:#fff"><span class="sq" style="background:#fff"></span>BrickWisely</div>
    <div class="col" style="left:92px;top:230px">
      <div class="lbl"><svg width="14" height="10" viewBox="0 0 14 10"><rect x="0.5" y="0.5" width="13" height="9" fill="#f29a1f"/><path d="M1 1l6 5 6-5" stroke="#0b1532" fill="none"/></svg>Email:</div>
      <div style="padding-left:26px;line-height:22px">marla@brickwisely.com<br>support@brickwisely.com</div>
    </div>
    <div class="rule" style="left:377px"></div>
    <div class="col" style="left:420px;top:144px;line-height:26px">
      <div class="lbl"><svg width="10" height="13" viewBox="0 0 10 13"><path d="M5 0a4.5 4.5 0 0 0-4.5 4.5C.5 8 5 13 5 13s4.5-5 4.5-8.5A4.5 4.5 0 0 0 5 0z" fill="#f29a1f"/></svg>Location:</div>
      <div style="padding-left:16px">412 Halden Street<br>Riverton, KS 66210</div>
      <div class="lbl" style="margin-top:20px"><svg width="11" height="11" viewBox="0 0 24 24"><path d="M6.6 10.8a15 15 0 0 0 6.6 6.6l2.2-2.2a1 1 0 0 1 1-.25 11 11 0 0 0 3.6.6 1 1 0 0 1 1 1V20a1 1 0 0 1-1 1A17 17 0 0 1 3 4a1 1 0 0 1 1-1h3.5a1 1 0 0 1 1 1 11 11 0 0 0 .6 3.6 1 1 0 0 1-.25 1z" fill="#f29a1f"/></svg>Phone:</div>
      <div style="padding-left:16px">(816) 555-0148</div>
    </div>
    <div class="rule" style="left:636px"></div>
    <div class="col" style="left:680px;top:144px;line-height:33px">Owners / Shareholders<br>Contractors<br>Construction Lawyers<br>Finance</div>
    <div class="rule" style="left:900px"></div>
    <div class="col" style="left:951px;top:144px;line-height:33px">Privacy policy<br>Terms &amp; Conditions<br>Disclaimer</div>
  </footer>

  <div class="legal">
    <div class="copy">©2022 <b>BrickWisely</b>.All Right Reserved</div>
    <div class="social"><i></i><i></i><i></i><i></i></div>
    <div class="certs">
      <span style="display:block;width:60px;height:34px;border-radius:17px;background:#c9d4e4"></span>
      <span style="display:block;width:130px;height:34px;background:#1d3b73"></span>
      <span style="display:block;width:40px;height:40px;border-radius:50%;background:#222"></span>
      <span style="display:block;width:40px;height:40px;border-radius:50%;background:#222"></span>
    </div>
  </div>

</div>
</body>
</html>
```